Email signature design - law firm

We are a small boutique law firm which is located near the beach in Manly, Australia.

We have just recently developed a new logo and are looking to redesign our letterhead, business cards and email signatures.

This brief is for our email signatures. This is an email signature to appear at the bottom of our Outlook emails so we would like it to be text that we are able to edit as the wording in our email signature often required amendments.

I have attached a word document which had our new logo, and our previous email signature which all the information/wording that needs to be included.

We would like multiple designs with a modern, simplistic yet striking look.

Thanks.

font - raleway or montserrat

Need extra days to review

• Must have the exact wording which appears in the email signature in the word document attached to brief.
• Must be able to edit the text as it is for an Outlook email signature which wording will change from time to time.

```html
<!DOCTYPE html>
<html lang="en">
<head>
<meta charset="utf-8">
<title>Email Signature – Harbourne &amp; Associates</title>
<link href="https://fonts.googleapis.com/css2?family=Raleway:wght@700&family=Lato:wght@400;700&display=swap" rel="stylesheet">
<style>
  :root {
    --page-bg: #f0f0f0;
    --card-bg: #ffffff;
    --brand-blue: #6478b4;
    --name-tint: #eef0fa;
    --ink: #1c1c1c;
    --icon-navy: #27336b;
  }
  html, body {
    margin: 0;
    padding: 0;
    width: 1200px;
    height: 757px;
    overflow: hidden;
    background: var(--page-bg);
  }
  .signature {
    position: absolute;
    left: 105px;
    top: 265px;
    width: 989px;
    height: 227px;
    background: var(--card-bg);
    font-family: "Lato", Arial, sans-serif;
    color: var(--ink);
  }
  .signature__bands {
    position: absolute;
    inset: 0;
  }
  .signature__bands polygon { fill: var(--brand-blue); }
  .signature__header {
    position: absolute;
    left: 51px;
    top: 10px;
    height: 36px;
    display: flex;
    align-items: baseline;
    gap: 12px;
    white-space: nowrap;
  }
  .signature__name {
    font-family: "Raleway", Arial, sans-serif;
    font-weight: 700;
    font-size: 30px;
    color: var(--name-tint);
    letter-spacing: 0.2px;
  }
  .signature__role {
    font-size: 22px;
    color: var(--ink);
  }
  .contact-list {
    position: absolute;
    left: 51px;
    top: 76px;
    margin: 0;
    padding: 0;
    list-style: none;
  }
  .contact-list__item {
    display: flex;
    align-items: center;
    height: 42px;
    font-size: 22px;
    white-space: nowrap;
  }
  .contact-list__icon {
    width: 26px;
    height: 26px;
    margin-right: 14px;
    flex: none;
  }
  .contact-list__icon * { fill: var(--icon-navy); }
  .firm-mark {
    position: absolute;
    left: 680px;
    top: 26px;
    width: 260px;
    display: flex;
    flex-direction: column;
    align-items: center;
    gap: 18px;
  }
  .firm-mark__dot {
    width: 92px;
    height: 92px;
    border-radius: 50%;
    background: var(--brand-blue);
  }
  .firm-mark__name {
    font-family: "Lato", Arial, sans-serif;
    font-weight: 700;
    font-size: 21px;
    letter-spacing: 1px;
    color: var(--ink);
    white-space: nowrap;
  }
</style>
</head>
<body>
  <section class="signature">
    <svg class="signature__bands" width="989" height="227" viewBox="0 0 989 227" aria-hidden="true">
      <polygon points="0,0 656,0 600,56 0,56"/>
      <polygon points="446,208 989,208 989,227 466,227"/>
    </svg>

    <header class="signature__header">
      <span class="signature__name">NADIA FENWICK</span>
      <span class="signature__role">Practise Manager</span>
    </header>

    <ul class="contact-list">
      <li class="contact-list__item">
        <svg class="contact-list__icon" viewBox="0 0 24 24" aria-hidden="true">
          <path d="M2 9c0-3 4-5 10-5s10 2 10 5v2h-5V8.5c-1.5-.6-3.2-.9-5-.9s-3.5.3-5 .9V11H2z"/>
          <path d="M5 12l2-3h10l2 3v8H5zm7 1.5a2.5 2.5 0 1 0 0 5 2.5 2.5 0 0 0 0-5z"/>
        </svg>
        <span>(022) 9000 4180</span>
      </li>
      <li class="contact-list__item">
        <svg class="contact-list__icon" viewBox="0 0 24 24" aria-hidden="true">
          <path d="M1 5h22v14H1zm2 2v.4l9 6.2 9-6.2V7zm0 2.8V17h18V9.8l-9 6.2z"/>
        </svg>
        <span>nadia.fenwick@harbournelegal.com.au</span>
      </li>
      <li class="contact-list__item">
        <svg class="contact-list__icon" viewBox="0 0 24 24" aria-hidden="true">
          <path d="M12 1a11 11 0 1 0 0 22 11 11 0 0 0 0-22zm-1 3c-.5 1.5-2.5 2-3 3.5s1 2 2.5 2.5 1 2.5 0 3.5-.5 3 .5 4.5c-4-.5-7-3.8-7-8 0-3 1.6-5.5 4-7zm3 .2c3.3.9 6 4 6 7.8 0 1.5-.4 2.9-1.1 4.1-.6-1.3-2-1.6-2.9-2.6s.3-2.5-1-3.5-2.8.2-3.5-1 .9-2.3 2.5-2.5z"/>
        </svg>
        <span>www.harbournelegal.com.au</span>
      </li>
    </ul>

    <div class="firm-mark">
      <span class="firm-mark__dot" aria-hidden="true"></span>
      <span class="firm-mark__name">Harbourne &amp; Associates</span>
    </div>
  </section>
</body>
</html>
```